Postcard design to acquire new clients for my Property Management Company

I'm looking for a postcard design that I can send to prospective clients detailing information about my company and services.
Postcard should be eye catching and contain information from www.brightkeeplm.com. I've provided a few screen shots for the most important information and my logo.
Target Market(s)
Real Estate
Industry/Entity Type
Real Estate
Font styles to use
Sans Serif
Requirements
Must have
- Must be eye catching!! this will be a direct mail piece - I'd like for the card to be read and not tossed in the trash immediately.
Design que from the logo.
A place to write / print the receipts name and address.
our physical address - 2287 Marden Lane, Lubbock, TX 79382.
Should not have
- the contact information on the business card is not accurate - please use info from website.

```html
<!DOCTYPE html>
<html lang="en">
<head>
<meta charset="utf-8">
<title>Brightkeep Property Management – Postcard</title>
<link href="https://fonts.googleapis.com/css2?family=Montserrat:wght@400;500;600;700;800&family=Arimo:wght@400&display=swap" rel="stylesheet">
<style>
  :root{
    --navy:#0d3f86;
    --navy-deep:#0a2f6a;
    --blue:#1d4fa6;
    --band:#2447a8;
    --ink:#151515;
    --grey-bar:#8a8a8a;
    --dark:#3a3a3a;
    --paper:#ffffff;
    --mist:#eef0f4;
    --stage:#707070;
  }
  *{box-sizing:border-box;margin:0;padding:0}
  html,body{width:846px;height:1200px;overflow:hidden}
  body{background:var(--stage);font-family:'Montserrat',sans-serif;position:relative}
  .card{position:absolute;left:79px;width:689px;height:493px;background:var(--paper);overflow:hidden}
  .front{top:73px}
  .back{top:633px;background:linear-gradient(135deg,#f1f2f5 0%,#ffffff 55%)}

  /* front */
  .hero{position:absolute;left:0;top:0;width:689px;height:290px;background:linear-gradient(180deg,#123d80 0%,#1b4d8f 55%,#2a5a83 100%)}
  .brand{position:absolute;left:69px;top:38px;color:#fff}
  .brand-name{font-weight:800;font-size:35px;letter-spacing:9px;line-height:1}
  .brand-sub{font-weight:500;font-size:16px;letter-spacing:5.3px;margin-top:8px}
  .headline-frame{position:absolute;left:69px;top:131px;width:550px;height:68px;border:2px solid #fff;border-bottom:none;border-radius:6px 6px 0 0}
  .headline-frame::before,.headline-frame::after{content:"";position:absolute;bottom:0;height:2px;background:#fff}
  .headline-frame::before{left:-2px;width:82px}
  .headline-frame::after{right:-2px;width:80px}
  .headline{position:absolute;left:69px;width:550px;top:140px;text-align:center;color:#fff;font-weight:800;font-size:29px;line-height:38px}
  .tagline{position:absolute;left:0;width:689px;top:233px;text-align:center;color:#fff;font-weight:500;font-size:15px}
  .services-band{position:absolute;left:171px;top:284px;width:348px;height:35px;background:linear-gradient(180deg,#2b55b8,#1d3f96);border-radius:3px;color:#fff;font-weight:800;font-size:21px;text-align:center;line-height:35px}
  .service-row{position:absolute;left:0;top:0;width:689px;height:440px}
  .service{position:absolute;top:333px;width:80px;margin-left:-40px;text-align:center}
  .service-icon{width:62px;height:62px;margin:0 auto;border-radius:50%;border:1px dotted var(--navy);padding:3px}
  .service-icon svg{width:54px;height:54px;border-radius:50%;background:#fff;box-shadow:0 1px 4px rgba(0,0,0,.25);display:block}
  .service-label{color:var(--blue);font-weight:500;font-size:11.5px;line-height:13.5px;height:28px;display:flex;align-items:center;justify-content:center;margin-top:11px}
  .contact-strip{position:absolute;left:0;top:441px;width:689px;height:52px;background:var(--dark);border-top:3px solid var(--navy);color:#fff;display:flex;align-items:center;justify-content:center;gap:14px;font-size:15.5px;font-weight:500}
  .contact-strip .sep{opacity:.8}
  .contact-strip svg{width:13px;height:13px;vertical-align:-1px;margin-right:5px}

  /* back */
  .system-title{position:absolute;left:37px;top:33px;font-weight:800;font-size:21px;line-height:27px;color:var(--ink)}
  .system-title span{display:block;color:var(--navy)}
  .back-brand{position:absolute;left:367px;top:37px;color:var(--navy)}
  .back-brand .brand-name{font-size:19px;letter-spacing:5px}
  .back-brand .brand-sub{font-size:8.8px;letter-spacing:2.9px;margin-top:3px}
  .indicia{position:absolute;left:558px;top:39px;width:92px;height:73px;border:1px solid #333;font-family:'Arimo',sans-serif;font-size:10.3px;line-height:13.6px;text-align:center;padding-top:3px;color:#222}
  .divider{position:absolute;top:119px;width:1px;height:218px;background:var(--navy)}
  .plan{position:absolute;top:129px;width:140px;margin-left:-70px;text-align:center}
  .plan-name{width:113px;height:18px;margin:0 auto;background:var(--navy);color:#fff;font-weight:700;font-size:11px;line-height:18px}
  .plan-note{width:124px;height:14px;margin:0 auto;background:var(--grey-bar);color:#fff;font-weight:600;font-size:7.6px;line-height:14px}
  .plan-price{width:87px;height:45px;margin:0 auto;background:var(--navy);color:#fff;padding-top:1px}
  .plan-price b{display:block;font-weight:800;font-size:28px;line-height:30px}
  .plan-price small{display:block;font-size:7.5px;line-height:9px}
  .plan-list{list-style:none;margin-top:14px;font-size:8.3px;font-weight:500;color:var(--ink);line-height:14.7px;white-space:nowrap}
  .address-line{position:absolute;left:465px;width:184px;height:1px;background:#555}
  .contact-panel{position:absolute;left:0;top:0;width:689px;height:493px}
  .contact-title{position:absolute;left:37px;top:366px;color:#fff;font-weight:700;font-size:18.5px;padding-bottom:3px;border-bottom:1px solid #fff;width:234px}
  .contact-list{position:absolute;left:37px;top:401px;list-style:none;color:#fff;font-size:12.3px;line-height:18.4px}
  .contact-list svg{width:11px;height:11px;margin-right:8px;vertical-align:-1px}
  .social{position:absolute;left:241px;top:437px;width:70px;text-align:center;color:#fff;font-size:11px;font-weight:500}
  .social i{display:block;width:14px;height:14px;border:1.6px solid #fff;border-radius:50%;margin:0 auto 3px}
  .fair-badge{position:absolute;left:338px;top:449px;width:20px;height:18px;background:#fff;border-radius:2px}
</style>
</head>
<body>

<section class="card front">
  <div class="hero" role="img" aria-label="Dusk photograph of the Lubbock city skyline in deep blue tones"></div>
  <div class="brand">
    <div class="brand-name">BRIGHTKEEP</div>
    <div class="brand-sub">PROPERTY MANAGEMENT</div>
  </div>
  <div class="headline-frame"></div>
  <h1 class="headline">PROPERTY MANAGEMENT<br>ACROSS LUBBOCK, TX</h1>
  <p class="tagline">Maximize your financial returns with support from our rental specialists</p>
  <div class="services-band">DISCOVER OUR SERVICES</div>

  <div class="service-row">
    <div class="service" style="left:73px">
      <div class="service-icon"><svg viewBox="0 0 54 54" fill="none" stroke="#0d3f86" stroke-width="2"><path d="M15 27 27 16 39 27M19 24v13h6v-7h4v7h6V24"/></svg></div>
      <div class="service-label">Property<br>Marketing</div>
    </div>
    <div class="service" style="left:150px">
      <div class="service-icon"><svg viewBox="0 0 54 54" fill="none" stroke="#0d3f86" stroke-width="1.8"><circle cx="31" cy="21" r="5"/><path d="M23 37c0-6 4-9 8-9s8 3 8 9"/><rect x="14" y="22" width="8" height="7"/><circle cx="17" cy="34" r="3"/><path d="M20 34h9"/></svg></div>
      <div class="service-label">Tenant<br>Screening</div>
    </div>
    <div class="service" style="left:228px">
      <div class="service-icon"><svg viewBox="0 0 54 54" fill="none" stroke="#0d3f86" stroke-width="1.8"><rect x="14" y="21" width="26" height="15" rx="1"/><circle cx="27" cy="28.5" r="4"/><path d="M18 18h22v3"/></svg></div>
      <div class="service-label">Rent<br>Collection</div>
    </div>
    <div class="service" style="left:305px">
      <div class="service-icon"><svg viewBox="0 0 54 54" fill="none" stroke="#0d3f86" stroke-width="1.8"><circle cx="26" cy="26" r="9"/><circle cx="26" cy="26" r="4"/><path d="M26 13v4M26 35v4M13 26h4M35 26h4M31 31l8 8"/></svg></div>
      <div class="service-label">Maintenance</div>
    </div>
    <div class="service" style="left:383px">
      <div class="service-icon"><svg viewBox="0 0 54 54" fill="none" stroke="#0d3f86" stroke-width="1.8"><path d="M14 26 27 15 40 26M18 23v14h18V23"/><circle cx="26" cy="29" r="4"/><path d="M29 32l4 4"/></svg></div>
      <div class="service-label">Property<br>Inspections</div>
    </div>
    <div class="service" style="left:461px">
      <div class="service-icon"><svg viewBox="0 0 54 54" fill="none" stroke="#0d3f86" stroke-width="1.8"><rect x="14" y="16" width="26" height="18"/><path d="M21 30v-4M26 30v-7M31 30v-10M22 34l-3 5M32 34l3 5"/></svg></div>
      <div class="service-label">Financial<br>Reporting</div>
    </div>
    <div class="service" style="left:538px">
      <div class="service-icon"><svg viewBox="0 0 54 54" fill="none" stroke="#0d3f86" stroke-width="1.8"><path d="M27 13l11 4v9c0 7-5 11-11 14-6-3-11-7-11-14v-9z"/><path d="M21 27l6-5 6 5M23 25v6h8v-6"/></svg></div>
      <div class="service-label">Evictions</div>
    </div>
    <div class="service" style="left:616px">
      <div class="service-icon"><svg viewBox="0 0 54 54" fill="none" stroke="#0d3f86" stroke-width="1.8"><path d="M27 14v24M20 38h14M16 20h22M16 20l-4 9h8zM38 20l-4 9h8z"/></svg></div>
      <div class="service-label">Legal<br>Guidance</div>
    </div>
  </div>

  <div class="contact-strip">
    <span><svg viewBox="0 0 14 14" fill="none" stroke="#fff" stroke-width="1.2"><circle cx="7" cy="7" r="6"/><path d="M1 7h12M7 1c-3 3-3 9 0 12M7 1c3 3 3 9 0 12"/></svg>www.brightkeeplm.com</span>
    <span class="sep">|</span>
    <span><svg viewBox="0 0 14 14" fill="none" stroke="#fff" stroke-width="1.2"><rect x="1" y="3" width="12" height="8"/><path d="M1 3l6 5 6-5"/></svg>info@brightkeeplm.com</span>
    <span class="sep">|</span>
    <span><svg viewBox="0 0 14 14" fill="none" stroke="#fff" stroke-width="1.2"><circle cx="7" cy="7" r="6"/><path d="M5 4l1 2-1 1c.5 1 1 1.5 2 2l1-1 2 1-1 1.5c-2 0-4.5-2.5-4.5-4.5z"/></svg>(806) 555-0147</span>
  </div>
</section>

<section class="card back">
  <h2 class="system-title">CHOOSE THE RIGHT<span>PROPERTY MANAGEMENT</span><span>SYSTEM</span></h2>
  <div class="back-brand">
    <div class="brand-name">BRIGHTKEEP</div>
    <div class="brand-sub">PROPERTY MANAGEMENT</div>
  </div>
  <div class="indicia">PRSRT STD<br>ECRWSS<br>U.S. POSTAGE<br>PAID<br>EDDM RETAIL</div>

  <div class="divider" style="left:186px"></div>
  <div class="divider" style="left:341px"></div>

  <div class="plan" style="left:105px">
    <div class="plan-name">Lease Only</div>
    <div class="plan-note">You Just Need Tenants</div>
    <div class="plan-price"><b>9%</b><small>of annual lease</small></div>
    <ul class="plan-list">
      <li>Professional Photography</li><li>Marketing &amp; Advertising</li><li>Property Showings</li><li>Tenant Screening &amp; Qualifications</li><li>Lease Execution</li><li>Move In Coordination</li>
    </ul>
  </div>
  <div class="plan" style="left:263px">
    <div class="plan-name">Full Service</div>
    <div class="plan-note">Our Most Popular</div>
    <div class="plan-price"><b>10%</b><small>of monthly rent</small></div>
    <ul class="plan-list" style="margin-top:12px">
      <li>Includes Leasing Service</li><li>24/7 Emergency Response</li><li>Move In &amp; Out Inspections</li><li>Professional Lease Enforcement</li><li>Schedule &amp; Oversee all Repairs</li><li>Pay all Invoices</li><li>Monthly &amp; Year End Statements</li><li>Annual Market Rent Analysis</li>
    </ul>
  </div>
  <div class="plan" style="left:416px">
    <div class="plan-name">Premium Service</div>
    <div class="plan-note">Our Premier Service</div>
    <div class="plan-price"><b>12%</b><small>of monthly rent</small></div>
    <ul class="plan-list" style="margin-top:12px">
      <li>Includes Full Service Features</li><li>Professional Video Marketing</li><li>Home Warranty Coordination</li><li>Tenant Retention Program</li>
    </ul>
  </div>

  <div class="address-line" style="top:318px"></div>
  <div class="address-line" style="top:352px"></div>
  <div class="address-line" style="top:386px"></div>

  <svg class="contact-panel" viewBox="0 0 689 493" aria-hidden="true">
    <polygon points="0,354 327,354 415,493 0,493" fill="#0d3f86"/>
    <rect x="0" y="489" width="689" height="4" fill="#0d3f86"/>
  </svg>
  <h3 class="contact-title">Contact Our Team</h3>
  <ul class="contact-list">
    <li><svg viewBox="0 0 12 12" fill="none" stroke="#fff" stroke-width="1.1"><path d="M6 11S2 6.5 2 4.5a4 4 0 0 1 8 0C10 6.5 6 11 6 11z"/><circle cx="6" cy="4.5" r="1.4"/></svg>2287 Marden Lane, Lubbock, TX 79382</li>
    <li><svg viewBox="0 0 12 12" fill="none" stroke="#fff" stroke-width="1.1"><circle cx="6" cy="6" r="5"/><path d="M4.3 3.5l.9 1.7-.8.8c.4.8.9 1.3 1.7 1.7l.8-.8 1.7.9-.9 1.2C5.9 9 3.1 6.3 3.1 4.4z"/></svg>(806) 555-0147</li>
    <li><svg viewBox="0 0 12 12" fill="none" stroke="#fff" stroke-width="1.1"><rect x="1" y="2.5" width="10" height="7"/><path d="M1 2.5l5 4 5-4"/></svg>info@brightkeeplm.com</li>
    <li><svg viewBox="0 0 12 12" fill="none" stroke="#fff" stroke-width="1.1"><circle cx="6" cy="6" r="5"/><path d="M1 6h10M6 1c-2.5 2.5-2.5 7.5 0 10M6 1c2.5 2.5 2.5 7.5 0 10"/></svg>www.brightkeeplm.com</li>
  </ul>
  <div class="social"><i></i>brightkeeplm</div>
  <div class="fair-badge" role="img" aria-label="Housing badge"></div>
</section>

</body>
</html>
```